VELQUARTH - A modern gin bottle label

Design of a bottle label in a modern fresh design. The name of the gin is "VELQUARTH Hollow Batch K7". Please take a look at the velquarth.de website. on the main page of velquarth.de you can breathe the design direction here: 1) the taste of the gin should be composed of 10 botanicals ... an important scent note. ) a distinctive flavor is spicy and fresh 3.) The filling volume is 0.5 liters 4.) the alcohol content is 43% vol. 5.) the variety is called "dry gin" 6.) velquarth stands for "energy" and "love"

Target Market(s)

Alcohol consumer

Colors

Designer to choose colors to be used in the design.

Requirements
Must have
• the velquarth corporate logo must be included, the name of the gin is "VELQUARTH Hollow Batch K7"
Nice to have
• Please use the bottles template in the appendix. (The Black Bottles) they can use the saying "DESTILLED & BOTTLED BY OLD MARROW" in small letters

```html
<!DOCTYPE html>
<html lang="en">
<head>
<meta charset="utf-8">
<title>VELQUARTH Hollow Batch K7 – Dry Gin Label</title>
<link rel="stylesheet" href="https://fonts.googleapis.com/css2?family=Orbitron:wght@600;700&family=Exo+2:wght@500;600&display=swap">
<style>
  :root {
    --label-black: #0e0e0f;
    --label-charcoal: #1d1d1f;
    --gold: #b9894a;
    --gold-deep: #9a6b32;
    --warm-glow: rgba(170, 110, 40, 0.28);
    --ornament-tone: rgba(123, 123, 126, 0.22);
    --mark-grey: #c9c9cc;
    --mark-rust: #a8451f;
  }
  * { margin: 0; padding: 0; box-sizing: border-box; }
  html, body {
    width: 776px;
    height: 1200px;
    overflow: hidden;
    background: var(--label-black);
  }
  .label {
    position: relative;
    width: 776px;
    height: 1200px;
    background:
      radial-gradient(ellipse 260px 150px at 50% 700px, var(--warm-glow), transparent 70%),
      radial-gradient(ellipse 520px 700px at 50% 520px, var(--label-charcoal), var(--label-black) 80%);
    font-family: "Exo 2", sans-serif;
    color: var(--gold);
    text-align: center;
  }
  .variety {
    position: absolute;
    top: 262px;
    left: 0;
    width: 100%;
    font-size: 30px;
    font-weight: 600;
    letter-spacing: 5px;
  }
  .ornament-area {
    position: absolute;
    top: 404px;
    left: 150px;
    width: 476px;
    height: 240px;
    background: radial-gradient(ellipse 50% 55% at 50% 70%, var(--ornament-tone), transparent 100%);
  }
  .gin-name {
    position: absolute;
    top: 648px;
    left: 0;
    width: 100%;
    font-family: "Orbitron", sans-serif;
    font-weight: 700;
    font-size: 64px;
    line-height: 1.2;
    letter-spacing: 4px;
    color: var(--gold);
  }
  .edition {
    position: absolute;
    top: 752px;
    left: 0;
    width: 100%;
    font-family: "Orbitron", sans-serif;
    font-weight: 600;
    font-size: 29px;
    line-height: 1.2;
    letter-spacing: 5px;
    color: var(--gold-deep);
  }
  .maker-mark {
    position: absolute;
    top: 985px;
    left: 0;
    width: 100%;
    display: flex;
    justify-content: center;
    align-items: center;
    gap: 10px;
  }
  .maker-mark .dot {
    width: 14px;
    height: 14px;
    background: var(--mark-rust);
  }
  .maker-mark .name {
    font-family: "Exo 2", sans-serif;
    font-weight: 600;
    font-size: 20px;
    letter-spacing: 3px;
    color: var(--mark-grey);
  }
  .spec {
    position: absolute;
    top: 1060px;
    font-family: "Orbitron", sans-serif;
    font-weight: 600;
    font-size: 27px;
    letter-spacing: 2px;
    color: var(--gold-deep);
  }
  .spec.abv { left: 132px; }
  .spec.volume { right: 128px; }
  .spec.volume .unit { font-size: 17px; vertical-align: 10px; margin-left: 4px; }
</style>
</head>
<body>
  <main class="label">
    <p class="variety">DRY GIN</p>

    <div class="ornament-area" role="img" aria-label="Decorative ornament of thin curved grey lines above the gin name"></div>

    <h1 class="gin-name">VELQUARTH</h1>
    <p class="edition">HOLLOW BATCH K7</p>

    <div class="maker-mark">
      <span class="dot"></span>
      <span class="name">VELQUARTH</span>
    </div>

    <p class="spec abv">43%</p>
    <p class="spec volume">0.5<span class="unit">LT</span></p>
  </main>
</body>
</html>
```